Professional Lawn Treatment flyer (double sided) needed for established gardening company

We are an established and trusted gardening company in Swindon, UK, and are about to launch a new Lawn Treatment Service. This will be marketed to both existing and new customers and needs to reflect our current professional image. The flyer will need to be double-sided, portrait orientation and correctly sized so to be printed on A5.

If you look on our website www.tavistrowgardening.co.uk, you will see our colours are purple and green. We would like you to use these exact shades of purple and green in your design.

As part of the design, we will need you to put together an infographic table to show our packages. I have attached a spreadsheet which explains these packages but I will need you to create a visually appealing table that fits in with the overall design of the flyer. I don't want you to simply cut and paste my basic table into the design.

In terms of what needs to be included, I have tried to be as specific as possible here but please feel free to message me if you need any further information or clarification.

FRONT SIDE:
The title of our service is:
Expert Lawn Treatment Service

Our strapline will need to be included somewhere:
"Lawn care by your local gardening expert"

The front side of the flyer will need to contain our logo - different versions of which can be found within my dropbox folder here...

https://www.sharebinnu.co.uk/sh/k7qd21mzplax/QRT8xWbnNeLu4Pa-ZxYyhKcLo?dl=0

The front side will need to contain a main image (although feel free to add more if you have anything suitable). I have included a picture in the dropbox folder titled "Front side image" which we would like used. I've also included in the folder an adobe image of grass which you may or may not like to use on either front or back.

Somewhere on both the front and back sides, you will need to include our contact details:
01632 960417
www.tavistrowgardening.co.uk/lawncare

The front side should show what treatments we currently have available. These are:

- Lawn Fertilising
- Scarification
- Aeration
- Weed Control
- Moss Control
- Hydration Booster
- PlumeRest
- Turfing & Renovation

"Select a one-off treatment or choose from one of our specially created lawn care packages."

BACK SIDE:
On the back, we will still need our logo and contact details but the image we'd like used should be the one in the dropbox folder titled "Back side image". Again, if you have any other images you feel would also work, then please feel free to add them.

The back side is to contain a bit more information and be a bit 'wordier' and so can you please include the following 2 paragraphs:

"As expert gardeners, we are passionate about horticulture and working to bring out the very best in your garden. When we work in your garden, we look at it and treat it with the same care and attention as if it were our own, before handing it back for you to enjoy. Our passion doesn't end at just trees and shrubs though. Your grass is as much of a living, breathing plant as your shrubs and we therefore utilise our expert horticultural knowledge to ensure your lawn thrives and reaches its fullest potential.

Lawn care isn't just about applying a fertiliser. It's about really understanding your lawn and being able to use extensive knowledge and experience to diagnose and treat issues. It therefore stands to reason that you should employ an expert to bring out the best in your lawn which is why we at Tavistrow Gardening Services have created a superior lawn care service that will keep your lawn looking lush, green and healthy all year round."

I referred at the very top of this brief to the fact we will need an infographic table created to show the different lawn care packages available. You see from the PDF table I created that we have 3 packages; Standard, Enhanced and Premium. Please create a visually appealing table which sets out the differences between our packages and include it on the back page.

Finally, somewhere we would like reference to the other gardening services we do. It's only to be something small as it isn't the main focus of the flyer but we think it would be good to mention what else we do. To re-iterate, it isnt to be big. I still want the main focus to be lawn care but if you could somehow reference that we also do the following services, that would be good. I will leave it to you to decide where on the flyer it fits in best, be it the front or back:

- Lawn mowing
- Shrub pruning
- Hedge trimming
- Weed killing
- Garden clearance & tidy-up
- Planting & design
- Regular Garden Maintenance
- Turfing
- Fencing
- Gutter clearance

I think thats it. I look forward to your designs!
Ps. Don't forget the dropbox folder:

Target Market(s)

Professional men/women aged 25+
Retired aged 65+

Industry/Entity Type

Home And Garden

Font styles to use
Sans Serif

Colors
6b449b
9bcb3c

Requirements
Must have
• Our company colours; purple and green; as per our website www.tavistrowgardening.co.uk. I've selected purple and green on this brief just to highlight the colours needed but please be sure to use the exact shades from our website and NOT the shade of purple and green that were selected on this brief.
• All the wording as explained in the main project brief.
Nice to have
• I want the flyer to be bold, eye-catching and modern.
• We particularly like the font Trebuchet MS for general copy but please feel free to use any other font for bolder, main titles.
Should not have
• We don't want anything gimmicky. No cheesy marketing.
• We only want professional looking designs. With the greatest of respect, if you're just starting out or don't really do design but think you'll use this as practise, please don't waste your or our time. We've previously run contests for other projects where we've had designs submitted that have clearly been done on MS Word and used Clipart and Wordart. That's really not what we are looking for.

```html
<!DOCTYPE html>
<html lang="en">
<head>
<meta charset="utf-8">
<title>Expert Lawn Treatment Service — Tavistrow Gardening Services</title>
<link href="https://fonts.googleapis.com/css2?family=Inter:ital,wght@0,300;0,400;0,500;0,600;0,700;1,400&display=swap" rel="stylesheet">
<style>
  :root {
    --purple: #6b449b;
    --purple-soft: #a48bc8;
    --green: #9bcb3c;
    --green-pale: #eef5e6;
    --ink: #1d1d1d;
    --grey: #5a5a5a;
    --bark: #3b2a1e;
    --white: #ffffff;
  }
  * { margin: 0; padding: 0; box-sizing: border-box; }
  html, body { width: 846px; height: 1200px; overflow: hidden; }
  body { font-family: "Inter", Helvetica, Arial, sans-serif; background: var(--green-pale); }

  .flyer { position: relative; width: 846px; height: 1200px; background: var(--green-pale); overflow: hidden; }

  .hero {
    position: absolute; left: 0; top: 0; width: 846px; height: 528px; overflow: hidden;
  }
  .hero-photo {
    position: absolute; inset: 0;
    background:
      linear-gradient(200deg, transparent 30%, rgba(205,200,190,0.85) 48%, rgba(190,185,175,0.8) 62%, transparent 78%),
      linear-gradient(180deg, #6d8f4a 0%, #4f9a2a 18%, #49a424 55%, #3c8e1e 100%);
  }
  .strapline {
    position: absolute; left: 520px; top: 96px; width: 290px;
    color: var(--white); font-style: italic; font-size: 21px; line-height: 27px; text-align: center;
  }
  .title {
    position: absolute; left: 40px; top: 240px;
    color: var(--white); font-size: 82px; line-height: 72px; letter-spacing: -1px; text-transform: uppercase;
  }
  .title .light { font-weight: 300; display: block; }
  .title .bold { font-weight: 600; display: block; }

  .panel {
    position: absolute; left: 40px; top: 528px; width: 764px; height: 631px;
    background: var(--white); border: 2px solid var(--green); border-top: none;
  }

  .contact { position: absolute; right: 414px; top: 38px; text-align: right; }
  .section-label { font-size: 17.5px; font-weight: 700; color: var(--ink); letter-spacing: 0.2px; }
  .contact .phone { font-size: 32px; font-weight: 700; color: var(--green); margin-top: 6px; line-height: 36px; }
  .contact .web { font-size: 16px; font-weight: 500; color: var(--ink); margin-top: 2px; }

  .treatments { position: absolute; left: 388px; top: 38px; }
  .treatment-list { list-style: none; margin-top: 6px; }
  .treatment-list li { font-size: 34px; line-height: 36.4px; font-weight: 400; color: var(--purple-soft); }
  .treatment-list li:nth-child(even) { color: var(--purple); font-weight: 500; }
  .packages-note {
    margin-top: 16px; margin-left: 5px; width: 330px;
    font-size: 16px; line-height: 22px; color: var(--grey);
  }

  .tree-art {
    position: absolute; left: 0; top: 852px; width: 332px; height: 348px;
    background: radial-gradient(ellipse at 55% 38%, rgba(155,203,60,0.55) 0%, rgba(120,190,50,0.35) 45%, rgba(238,245,230,0) 72%);
  }

  .brand {
    position: absolute; left: 428px; top: 1030px; display: flex; align-items: center; gap: 12px;
  }
  .brand-dot { width: 34px; height: 34px; border-radius: 50%; background: var(--green); flex: none; }
  .brand-name { font-size: 24px; line-height: 28px; font-weight: 600; color: var(--bark); width: 200px; }
</style>
</head>
<body>
  <main class="flyer">
    <section class="hero">
      <div class="hero-photo" role="img" aria-label="Photograph of a winding stone paved path through a lush green lawn with shrubs and benches"></div>
      <p class="strapline">“Lawn care by your local gardening expert”</p>
      <h1 class="title">
        <span class="light">Expert</span>
        <span class="bold">Lawn</span>
        <span class="bold">Treatment</span>
        <span class="light">Service</span>
      </h1>
    </section>

    <section class="panel">
      <div class="contact">
        <h2 class="section-label">CONTACT US:</h2>
        <p class="phone">01632 960417</p>
        <p class="web">www.tavistrowgardening.co.uk</p>
      </div>

      <div class="treatments">
        <h2 class="section-label">AVAILABLE TREATMENTS:</h2>
        <ul class="treatment-list">
          <li>Lawn Fertilising</li>
          <li>Scarification</li>
          <li>Aeration</li>
          <li>Weed Control</li>
          <li>Moss Control</li>
          <li>Hydration Booster</li>
          <li>PlumeRest</li>
          <li>Turfing &amp; Renovation</li>
        </ul>
        <p class="packages-note">“Select a one-off treatment or choose from one of our specially created lawn care packages.”</p>
      </div>
    </section>

    <div class="tree-art" role="img" aria-label="Illustration of a stylised tree with green and lime leaves"></div>

    <div class="brand">
      <span class="brand-dot"></span>
      <span class="brand-name">Tavistrow Gardening Services</span>
    </div>
  </main>
</body>
</html>
```